Bref créative
TORV stationery
Stationery
Simple
Marco Daniel Fervone Lusse de Telvin
Administrador
Rua das Acácias nº17 Luanda-Angola
marco.telvin@torv-exemplo.com
www.torv-exemplo.com

```html
<!DOCTYPE html>
<html lang="pt">
<head>
<meta charset="utf-8">
<title>TORV — Cartão de visita</title>
<link href="https://fonts.googleapis.com/css2?family=Share+Tech&display=swap" rel="stylesheet">
<style>
  :root {
    --backdrop: #f1f1f1;
    --card-light: #ffffff;
    --card-mist: #e4e5e7;
    --orange-deep: #e0620e;
    --orange-mid: #f28a1a;
    --orange-glow: #fbb83a;
    --ink: #2b2b2b;
    --ink-soft: #3a3a3a;
    --accent-blue: #1f7fc4;
    --paper: #ffffff;
  }
  * { margin: 0; padding: 0; box-sizing: border-box; }
  html, body {
    width: 1200px; height: 799px; overflow: hidden;
    background: var(--backdrop);
    font-family: "Share Tech", sans-serif;
  }
  .business-card {
    position: absolute; left: 132px; top: 132px;
    width: 936px; height: 535px; overflow: hidden;
    background: var(--card-light);
  }
  .card-art { position: absolute; inset: 0; }
  .brand {
    position: absolute; left: 36px; top: 89px;
    display: flex; flex-direction: column; align-items: flex-start; gap: 10px;
  }
  .brand-mark {
    width: 130px; height: 130px; background: var(--orange-mid);
  }
  .brand-name {
    font-size: 62px; line-height: 1; color: var(--ink-soft); letter-spacing: 2px;
  }
  .holder {
    position: absolute; right: 196px; top: 228px; text-align: right;
  }
  .holder-name { font-size: 24px; color: var(--ink); letter-spacing: 0.2px; }
  .holder-role { font-size: 14px; color: var(--accent-blue); margin-top: 2px; }
  .contact {
    position: absolute; left: 36px; top: 390px;
    font-size: 15.5px; line-height: 22px; color: var(--ink-soft); list-style: none;
  }
  .website {
    position: absolute; left: 895px; top: 130px;
    writing-mode: vertical-rl;
    font-size: 18px; letter-spacing: 5px; color: var(--paper);
  }
</style>
</head>
<body>
  <main class="business-card">
    <svg class="card-art" viewBox="0 0 936 535" aria-hidden="true">
      <defs>
        <radialGradient id="paperShade" cx="0.3" cy="0.45" r="0.8">
          <stop offset="0" stop-color="var(--card-light)"/>
          <stop offset="1" stop-color="var(--card-mist)"/>
        </radialGradient>
        <linearGradient id="orangeBand" x1="0" y1="0" x2="1" y2="0">
          <stop offset="0" stop-color="var(--orange-glow)"/>
          <stop offset="0.35" stop-color="var(--orange-mid)"/>
          <stop offset="1" stop-color="var(--orange-deep)"/>
        </linearGradient>
      </defs>
      <rect width="936" height="535" fill="url(#paperShade)"/>
      <path d="M735 0 C840 120 850 360 700 535 L936 535 L936 0 Z" fill="url(#orangeBand)"/>
      <g fill="none" stroke="var(--paper)" stroke-width="1.4" opacity="0.85">
        <path d="M745 0 C855 130 860 370 712 535"/>
        <path d="M760 0 C870 150 860 390 728 535"/>
        <path d="M720 0 C820 110 835 350 690 535" stroke="var(--orange-mid)"/>
        <path d="M700 0 C810 140 820 380 670 535" stroke="var(--orange-glow)" opacity="0.6"/>
      </g>
      <path d="M180 0 C420 40 620 130 700 250" fill="none" stroke="#cfd0d2" stroke-width="1" opacity="0.7"/>
    </svg>

    <div class="brand">
      <span class="brand-mark"></span>
      <span class="brand-name">TORV</span>
    </div>

    <div class="holder">
      <p class="holder-name">Marco Daniel Fervone Lusse de Telvin</p>
      <p class="holder-role">Administrador</p>
    </div>

    <ul class="contact">
      <li>Rua das Acácias nº17 Luanda-Angola</li>
      <li>Phone: +244 222 410 073</li>
      <li>Cell: +244 923 118 264</li>
      <li>Fax: +244 222 410 079</li>
      <li>Email: marco.telvin@torv-exemplo.com</li>
    </ul>

    <p class="website">www.torv-exemplo.com</p>
  </main>
</body>
</html>
```